Accounting & Tax Services in Edmonton, Canada-Needs Website Design & Improvement

I am starting my business for accounting and tax services in Canada. I have my website but not much happy with that. My services are for bookkeeping, accounting and tax services. We serve both individual and corporate clients. I am trying to bring new idea in the market for providing services at their facility or business. My existing website is www.qrmt.ca
Currently, this site is static but I want to improve it to dynamic or interactive in nature.

Target Market(s)

Edmonton and Surrounding Areas, Canada

Industry/Entity Type

Public Accounting

Logo Text

Harborline Ledger & Advisory Partners

Number of Pages Required

4 page

Font styles to use
Sans Serif

Colors

Designer to choose colors to be used in the design.

Requirements
Must have
• 4 Pages
• I a not sure what do we mean by coded and uncoded design. Need clarification
• Rest is explained in project description. It should have the ingredients to attract traffic in any professional website.
• Logo Design Text can be shortened, if required.
• Existing logo attached, just for reference.
Nice to have
• 5 Pages

```html
<!DOCTYPE html>
<html lang="en">
<head>
<meta charset="utf-8">
<title>Harborline Ledger & Advisory Partners</title>
<link rel="stylesheet" href="https://fonts.googleapis.com/css2?family=Open+Sans:wght@400;600&family=Roboto+Condensed:wght@400;700&family=Roboto:wght@400;500&display=swap">
<style>
:root{
  --teal:#4b90a5;
  --navy:#24567a;
  --band:#2c5f80;
  --ink:#222;
  --text:#555;
  --muted:#777;
  --light:#f1f1f1;
  --footer:#151515;
  --white:#fff;
}
*{box-sizing:border-box;margin:0;padding:0}
html,body{width:1200px;height:3046px;overflow:hidden}
body{position:relative;background:var(--white);font-family:"Open Sans",sans-serif;color:var(--text)}
.abs{position:absolute}
.heading{font-family:"Roboto",sans-serif;color:var(--ink);font-weight:400}

/* header */
.site-header{left:0;top:0;width:1200px;height:146px;background:var(--white)}
.brand{left:86px;top:38px;width:200px;display:flex;align-items:center;gap:10px}
.brand-mark{width:14px;height:14px;background:var(--navy);flex:none}
.brand-name{font-family:"Roboto",sans-serif;font-size:17px;line-height:20px;color:var(--navy);font-weight:500}
.contact-bar{right:86px;top:28px;display:flex;align-items:center;gap:26px;font-family:"Roboto",sans-serif;font-size:16px;color:#444}
.contact-bar .item{display:flex;align-items:center;gap:10px}
.ring{width:34px;height:34px;border:2px solid #556;border-radius:50%;display:flex;align-items:center;justify-content:center}
.socials{display:flex;gap:8px}
.socials span{width:20px;height:20px;display:block}
.main-nav{right:86px;top:82px;display:flex;gap:22px;font-family:"Open Sans",sans-serif;font-size:16px;color:#333}
.main-nav .active{color:var(--teal)}

/* hero */
.hero{left:0;top:146px;width:1200px;height:509px;background:linear-gradient(120deg,#c9cfd6 0%,#8f98a3 35%,#4c535b 60%,#cdd2d8 100%)}
.hero-title{left:0;top:350px;width:1200px;text-align:center;color:var(--white)}
.hero-title h1{font-family:"Roboto Condensed",sans-serif;font-weight:400;font-size:50px;letter-spacing:1px;line-height:58px}
.hero-title p{font-family:"Roboto Condensed",sans-serif;font-size:38px;line-height:46px}
.slider-arrows{left:1058px;top:558px;display:flex;gap:4px}
.slider-arrows span{width:24px;height:24px;border-radius:50%;background:#444;display:flex;align-items:center;justify-content:center}

/* welcome */
.welcome-title{left:0;top:747px;width:1200px;text-align:center;font-size:34px}
.welcome-text{left:175px;top:810px;width:850px;text-align:center;font-size:13.5px;line-height:25px;color:var(--muted)}
.service{top:934px;width:300px;text-align:center}
.service .icon{width:104px;height:104px;border-radius:50%;margin:0 auto;display:flex;align-items:center;justify-content:center}
.service h3{font-family:"Roboto",sans-serif;font-weight:400;font-size:24px;color:var(--ink);margin-top:18px}
.service p{font-size:14px;line-height:22px;color:var(--muted);margin:10px auto 0;width:250px}
.service a{display:block;font-size:13px;color:var(--navy);margin-top:6px;text-decoration:none}

/* what we do */
.what-band{left:0;top:1263px;width:1200px;height:460px;background:linear-gradient(100deg,#2f6586,#24587a 60%,#2b5f80)}
.what-copy{left:90px;top:1363px;width:580px;color:var(--white)}
.what-copy h2{font-family:"Roboto",sans-serif;font-weight:400;font-size:32px}
.what-copy h4{font-family:"Roboto",sans-serif;font-weight:400;font-size:22px;margin-top:14px}
.what-copy p{font-size:14px;line-height:26px;margin-top:6px}
.btn{display:inline-block;margin-top:26px;background:var(--teal);color:var(--white);font-size:14px;padding:8px 20px;border-radius:2px}
.what-photo{left:760px;top:1364px;width:248px;height:248px;border-radius:50%;border:3px solid #9fc2d3;background:radial-gradient(circle at 45% 40%,#e6eef3,#9bb3c4 60%,#5a7487)}

/* blog */
.blog-title{left:0;top:1812px;width:1200px;text-align:center;font-size:34px}
.post{top:1898px;width:312px}
.post .photo{width:312px;height:174px}
.post .meta{display:flex;margin-top:11px;font-size:12px}
.post .date{background:var(--teal);color:var(--white);padding:3px 14px}
.post .count{background:#2a2a2a;color:var(--white);padding:3px 8px;display:flex;align-items:center;gap:3px;margin-left:2px}
.post h5{font-family:"Open Sans",sans-serif;font-weight:400;font-size:16px;color:var(--ink);margin-top:12px}
.post p{font-size:12.5px;line-height:20px;color:var(--muted);margin-top:6px}
.post a{font-size:13px;color:var(--navy);text-decoration:none;display:block;margin-top:2px}

/* testimonials */
.testimonials{left:0;top:2325px;width:1200px;height:412px;background:var(--light)}
.testi-title{left:0;top:2400px;width:1200px;text-align:center;font-size:28px}
.testi{top:2500px;display:flex;gap:20px}
.avatar{width:94px;height:94px;border-radius:50%;background:linear-gradient(#cfd4d9,#7d8791);border:3px solid #fff;flex:none}
.quote{width:330px;font-size:12px;line-height:22px;color:var(--text);text-align:justify}
.quote .mark{color:var(--teal);font-size:22px;font-family:Georgia,serif;line-height:0}
.quote .who{font-size:11px;font-weight:600;color:#333;margin-top:10px;text-transform:uppercase}
.quote .role{font-size:12px;color:#444}

/* footer */
.site-footer{left:0;top:2737px;width:1200px;height:309px;background:var(--footer)}
.footer-brand{left:92px;top:2830px;display:flex;align-items:center;gap:10px}
.footer-brand .brand-mark{background:#fff}
.footer-brand .brand-name{color:#fff}
.fcol{top:2792px;color:#fff;font-size:12px}
.fcol h6{font-family:"Open Sans",sans-serif;font-weight:400;font-size:14px;margin-bottom:22px}
.fline{display:flex;gap:14px;margin-bottom:14px;line-height:20px}
.subscribe{display:flex;margin-top:14px}
.subscribe span{background:#fff;color:#999;width:140px;height:28px;padding:5px 8px;font-size:11px}
.subscribe b{background:var(--navy);color:#fff;font-weight:400;height:28px;padding:6px 8px;font-size:12px}
.fsocial{display:flex;gap:14px}
.fsocial span{width:22px;height:22px;border:2px solid #fff;border-radius:3px;display:block}
.footer-rule{left:80px;top:2966px;width:1040px;height:1px;background:#333}
.copyright{left:0;top:2992px;width:1200px;text-align:center;color:#fff;font-size:12px}
</style>
</head>
<body>

<header class="site-header abs">
  <div class="brand abs"><span class="brand-mark"></span><span class="brand-name">Harborline Ledger &amp;<br>Advisory Partners</span></div>
  <div class="contact-bar abs">
    <div class="item"><span class="ring"><svg width="16" height="16" viewBox="0 0 24 24"><path d="M6.6 10.8a15 15 0 006.6 6.6l2.2-2.2c.3-.3.7-.4 1-.2 1.1.4 2.3.6 3.6.6.6 0 1 .4 1 1V20c0 .6-.4 1-1 1A17 17 0 013 4c0-.6.4-1 1-1h3.5c.6 0 1 .4 1 1 0 1.3.2 2.5.6 3.6.1.3 0 .7-.2 1z" fill="#445"/></svg></span>780.555.0142</div>
    <div class="item"><span class="ring"><svg width="16" height="16" viewBox="0 0 24 24"><rect x="2" y="5" width="20" height="14" rx="2" fill="#445"/><path d="M3 6l9 7 9-7" stroke="#fff" stroke-width="2" fill="none"/></svg></span>hello@harborline-ledger.ca</div>
    <div class="socials"><span style="background:#3b5b98"></span><span style="background:#2aa3e0"></span><span style="background:#1a75b0"></span><span style="background:#d2342a"></span></div>
  </div>
  <nav class="main-nav abs">
    <span class="active">Home</span><span>Firm profile</span><span>Client services</span><span>Newsletters</span><span>Financial tools</span><span>Info centre</span><span>Contact us</span>
  </nav>
</header>

<section class="hero abs" role="img" aria-label="Photo of a businessman working on a laptop and calculator with a faint world map overlay"></section>
<div class="hero-title abs"><h1>HARBORLINE LEDGER</h1><p>Advisory Partners</p></div>
<div class="slider-arrows abs">
  <span><svg width="10" height="10" viewBox="0 0 10 10"><path d="M6.5 1.5L3 5l3.5 3.5" stroke="#fff" stroke-width="1.6" fill="none"/></svg></span>
  <span><svg width="10" height="10" viewBox="0 0 10 10"><path d="M3.5 1.5L7 5 3.5 8.5" stroke="#fff" stroke-width="1.6" fill="none"/></svg></span>
</div>

<h2 class="welcome-title heading abs">Welcome To Harborline Ledger</h2>
<p class="welcome-text abs">Welcome and thank you for visiting our website. At Harborline Ledger &amp; Advisory Partners, We have built our business so that it guarantees your success. In addition to providing you with a profile of our firm and the services we provide, this website has been designed to become a helpful resource tool to you, our valued clients and visitors.</p>

<div class="service abs" style="left:132px">
  <div class="icon" style="background:var(--teal)"><svg width="44" height="40" viewBox="0 0 44 40"><rect x="3" y="3" width="38" height="26" rx="2" fill="none" stroke="#fff" stroke-width="4"/><rect x="18" y="29" width="8" height="6" fill="#fff"/><rect x="12" y="34" width="20" height="4" fill="#fff"/></svg></div>
  <h3>Bookkeeping</h3>
  <p>Our firm endeavors to provide you with the highest quality of service</p>
  <a>Learn More -&gt;</a>
</div>
<div class="service abs" style="left:449px">
  <div class="icon" style="background:var(--navy)"><svg width="40" height="40" viewBox="0 0 40 40"><path d="M30 22v12H6V10h12" fill="none" stroke="#fff" stroke-width="3.5"/><path d="M16 26l2-7 15-15 5 5-15 15z" fill="#fff"/></svg></div>
  <h3>Accounting</h3>
  <p>Our firm endeavors to provide you with the highest quality of service</p>
  <a>Learn More -&gt;</a>
</div>
<div class="service abs" style="left:770px">
  <div class="icon" style="background:var(--teal)"><svg width="32" height="40" viewBox="0 0 32 40"><path d="M2 2h18l10 10v26H2z" fill="#fff"/><path d="M8 20h16M8 26h16M8 32h12" stroke="var(--teal)" stroke-width="2.5"/></svg></div>
  <h3>Tax Services</h3>
  <p>Our firm endeavors to provide you with the highest quality of service</p>
  <a>Learn More -&gt;</a>
</div>

<section class="what-band abs" role="img" aria-label="Faint photo of a desk with documents under a blue tint"></section>
<div class="what-copy abs">
  <h2>What We Do</h2>
  <h4>Neque porro quisquam est qui dolorem ipsum</h4>
  <p>Welcome and thank you for visiting our website. At Harborline Ledger and Advisory Partners, we have built our business so that it guarantees your success. In addition to providing you with a profile of our firm and the services we provide, this website has been designed to become a helpful resource tool to you, our valued clients and visitors.</p>
  <span class="btn">Read More</span>
</div>
<div class="what-photo abs" role="img" aria-label="Round photo of hands working on a laptop showing charts"></div>

<h2 class="blog-title heading abs">Latest Blog</h2>
<article class="post abs" style="left:96px">
  <div class="photo" role="img" aria-label="Photo of a businessman with rising chart graphics" style="background:linear-gradient(135deg,#2c2f33,#8a9199 60%,#3a3d42)"></div>
  <div class="meta"><span class="date">Dec 03</span><span class="count"><svg width="12" height="10" viewBox="0 0 12 10"><path d="M1 1h10v6H5l-3 2V7H1z" fill="none" stroke="#fff"/></svg>0</span></div>
  <h5>Neque porro quisquam dolorem</h5>
  <p>It has survived not only five centuries, but also the leap into electronic typesetting.</p>
  <a>Read More »</a>
</article>
<article class="post abs" style="left:443px">
  <div class="photo" role="img" aria-label="Photo of hands using a tablet with network graphics" style="background:linear-gradient(135deg,#dfe7ef,#8aa5be 55%,#c7d4e0)"></div>
  <div class="meta"><span class="date">Dec 03</span><span class="count"><svg width="12" height="10" viewBox="0 0 12 10"><path d="M1 1h10v6H5l-3 2V7H1z" fill="none" stroke="#fff"/></svg>0</span></div>
  <h5>Porro quisquam est qui</h5>
  <p>It has survived not only five centuries, but also the leap into electronic typesetting.</p>
  <a>Read More »</a>
</article>
<article class="post abs" style="left:797px">
  <div class="photo" role="img" aria-label="Photo of a businesswoman seated at an office desk" style="background:linear-gradient(135deg,#c9b9a4,#e4e0da 50%,#3d6e8e)"></div>
  <div class="meta"><span class="date">Dec 03</span><span class="count"><svg width="12" height="10" viewBox="0 0 12 10"><path d="M1 1h10v6H5l-3 2V7H1z" fill="none" stroke="#fff"/></svg>0</span></div>
  <h5>Dolorem ipsum quia dolor</h5>
  <p>It has survived not only five centuries, but also the leap into electronic typesetting.</p>
  <a>Read More »</a>
</article>

<section class="testimonials abs"></section>
<h2 class="testi-title heading abs">TESTIMONIALS</h2>
<div class="testi abs" style="left:116px">
  <div class="avatar" role="img" aria-label="Portrait of a client"></div>
  <div class="quote"><span class="mark">“</span> It is a long established fact that a reader will be distracted by the readable content of a page when looking at its layout. The point of using Lorem <span class="mark">”</span>
    <div class="who">Martin Aldous</div><div class="role">Dolorem ipsum quia</div></div>
</div>
<div class="testi abs" style="left:640px">
  <div class="avatar" role="img" aria-label="Portrait of a client"></div>
  <div class="quote"><span class="mark">“</span> It is a long established fact that a reader will be distracted by the readable content of a page when looking at its layout. The point of using Lorem <span class="mark">”</span>
    <div class="who">Lena Whitcombe</div><div class="role">Porro quisquam</div></div>
</div>

<footer class="site-footer abs"></footer>
<div class="footer-brand abs"><span class="brand-mark"></span><span class="brand-name">Harborline Ledger &amp;<br>Advisory Partners</span></div>
<div class="fcol abs" style="left:370px">
  <h6>CONTACT US</h6>
  <div class="fline"><svg width="10" height="14" viewBox="0 0 10 14"><path d="M5 0a5 5 0 015 5c0 4-5 9-5 9S0 9 0 5a5 5 0 015-5z" fill="#fff"/><circle cx="5" cy="5" r="2" fill="#151515"/></svg><span>Suite 210, 4471 Ridgeway Avenue<br>NW, Edmonton, AB</span></div>
  <div class="fline"><svg width="12" height="12" viewBox="0 0 24 24"><path d="M6.6 10.8a15 15 0 006.6 6.6l2.2-2.2c.3-.3.7-.4 1-.2 1.1.4 2.3.6 3.6.6.6 0 1 .4 1 1V20c0 .6-.4 1-1 1A17 17 0 013 4c0-.6.4-1 1-1h3.5c.6 0 1 .4 1 1 0 1.3.2 2.5.6 3.6.1.3 0 .7-.2 1z" fill="#fff"/></svg><span>(587) 555 0199</span></div>
  <div class="fline"><svg width="12" height="10" viewBox="0 0 24 18"><rect x="1" y="1" width="22" height="16" rx="2" fill="#fff"/><path d="M2 2l10 8 10-8" stroke="#151515" stroke-width="2" fill="none"/></svg><span>office@harborline-ledger.ca</span></div>
</div>
<div class="fcol abs" style="left:650px;width:220px">
  <h6>JOIN OUR MAILING LIST</h6>
  <div style="line-height:18px">Your about us information would fit here nicely.</div>
  <div class="subscribe"><span>Email address</span><b>Submit</b></div>
</div>
<div class="fcol abs" style="left:955px">
  <h6>FOLLOW US OUT THERE</h6>
  <div class="fsocial"><span></span><span></span><span></span><span></span></div>
</div>
<div class="footer-rule abs"></div>
<div class="copyright abs">Copyright © 2017 All Rights Reserved</div>

</body>
</html>
```